Commercial Construction Company

We need a business card design based on our current logo. We are a commercial general contractor based in Southern California that specializes in bank remodels. We would like to see designs that incorporate dark blue. The final design should portray an image of professionalism and quality.

If possible, I would like to add metallic foil to the design. Thank you

```html
<!DOCTYPE html>
<html lang="en">
<head>
<meta charset="utf-8">
<title>Harlow Commercial Builders – Business Card</title>
<link href="https://fonts.googleapis.com/css2?family=Roboto:wght@400;700;900&display=swap" rel="stylesheet">
<style>
  :root {
    --backdrop: #2a2a2c;
    --card-white: #ffffff;
    --brand-blue: #1d4c86;
    --brand-grey: #a7a7a8;
    --ink: #151515;
    --on-grey: #ffffff;
  }
  html, body {
    margin: 0;
    width: 1200px;
    height: 880px;
    overflow: hidden;
    background: var(--backdrop);
    font-family: "Roboto", Arial, sans-serif;
  }
  .canvas { position: relative; width: 1200px; height: 880px; }
  .card {
    position: absolute;
    width: 525px;
    height: 300px;
    border-radius: 22px;
    overflow: hidden;
    background: var(--card-white);
    box-shadow: 0 18px 40px rgba(0,0,0,.45);
  }
  .card-front { left: 90px; top: 110px; }
  .card-back  { left: 585px; top: 470px; }
  .card svg.waves { position: absolute; inset: 0; width: 100%; height: 100%; }

  .brand {
    position: absolute;
    display: flex;
    align-items: center;
    gap: 10px;
    color: var(--ink);
    font-weight: 900;
    text-transform: uppercase;
    letter-spacing: .5px;
    line-height: 1.05;
  }
  .brand-dot {
    flex: none;
    border-radius: 50%;
    background: var(--brand-blue);
  }
  .card-front .brand { left: 150px; top: 118px; font-size: 22px; }
  .card-front .brand-dot { width: 40px; height: 40px; }
  .card-back .brand { left: 46px; top: 64px; font-size: 16px; }
  .card-back .brand-dot { width: 30px; height: 30px; }

  .contact {
    position: absolute;
    right: 34px;
    top: 70px;
    text-align: right;
    color: var(--on-grey);
  }
  .contact-name { margin: 0; font-size: 24px; font-weight: 700; letter-spacing: 1px; }
  .contact-role { margin: 2px 0 0; font-size: 20px; font-weight: 400; letter-spacing: .5px; }
  .contact-icons { display: flex; justify-content: flex-end; gap: 5px; margin: 16px 6px 10px 0; }
  .contact-icons svg { width: 16px; height: 16px; }
  .contact-lines { margin: 0; padding: 0; list-style: none; font-size: 16px; line-height: 1.4; }
</style>
</head>
<body>
<main class="canvas">

  <section class="card card-front" aria-label="Card front">
    <svg class="waves" viewBox="0 0 525 300" aria-hidden="true">
      <path fill="var(--brand-blue)" d="M210,0 C270,40 340,34 410,30 C465,27 500,45 525,70 L525,0 Z"/>
      <path fill="var(--brand-grey)" d="M0,205 C70,178 150,172 205,192 C250,210 265,250 295,300 L0,300 Z"/>
    </svg>
    <div class="brand">
      <span class="brand-dot"></span>
      <span>Harlow Commercial<br>Builders</span>
    </div>
  </section>

  <section class="card card-back" aria-label="Card back">
    <svg class="waves" viewBox="0 0 525 300" aria-hidden="true">
      <path fill="var(--brand-blue)" d="M290,0 C345,40 350,120 318,185 C290,245 315,285 335,300 L525,300 L525,0 Z"/>
      <path fill="var(--brand-grey)" d="M310,0 C365,40 370,120 338,185 C310,245 335,285 355,300 L525,300 L525,0 Z"/>
    </svg>
    <div class="brand">
      <span class="brand-dot"></span>
      <span>Harlow Commercial<br>Builders</span>
    </div>
    <div class="contact">
      <p class="contact-name">Dana Mercer</p>
      <p class="contact-role">Founder &amp; CEO</p>
      <div class="contact-icons" aria-hidden="true">
        <svg viewBox="0 0 16 16"><circle cx="8" cy="8" r="7.5" fill="var(--brand-blue)"/><path d="M5 4.5l1.6-.4 1 2-1 .8a5 5 0 0 0 2.5 2.5l.8-1 2 1-.4 1.6C8 11 5 8 5 4.5z" fill="#fff"/></svg>
        <svg viewBox="0 0 16 16"><circle cx="8" cy="8" r="7.5" fill="var(--brand-blue)"/><rect x="4" y="5" width="8" height="6" fill="none" stroke="#fff" stroke-width="1.2"/><path d="M4 5l4 3.2L12 5" fill="none" stroke="#fff" stroke-width="1.2"/></svg>
        <svg viewBox="0 0 16 16"><circle cx="8" cy="8" r="7.5" fill="var(--brand-blue)"/><circle cx="8" cy="8" r="4.2" fill="none" stroke="#fff" stroke-width="1.1"/><path d="M3.8 8h8.4M8 3.8c-2 2.4-2 6 0 8.4M8 3.8c2 2.4 2 6 0 8.4" fill="none" stroke="#fff" stroke-width="1"/></svg>
      </div>
      <ul class="contact-lines">
        <li>+0012 3344 5566</li>
        <li>info@harlowbuild.com</li>
        <li>www.harlowbuild.com</li>
      </ul>
    </div>
  </section>

</main>
</body>
</html>
```